Local Internet service provider, www.tallow-linkworks.com I have attached a quick edit of one of our previous versions to give you an idea of what words we want on the brochures.

Industry/Entity Type

Internet Service Provider

Colors

Designer to choose colors to be used in the design.

Requirements
Must have
• All words in the attached basic brochure
Nice to have
• Pictures related to the internet

```html
<!DOCTYPE html>
<html lang="en">
<head>
<meta charset="utf-8">
<title>Tallow Linkworks Brochure</title>
<link href="https://fonts.googleapis.com/css2?family=Roboto:wght@400;500;700&family=Roboto+Condensed:wght@400;700&family=Oswald:wght@500;700&display=swap" rel="stylesheet">
<style>
:root{
  --orange:#f47b20;
  --dark:#232323;
  --darker:#1a1a1a;
  --ink:#222;
  --white:#fff;
  --page:#e9e9e9;
}
*{box-sizing:border-box;margin:0;padding:0}
html,body{width:1200px;height:1200px;overflow:hidden;background:var(--page);font-family:'Roboto',sans-serif}
.spread{position:absolute;left:30px;top:172px;width:1140px;height:855px;display:flex;box-shadow:0 10px 30px rgba(0,0,0,.2)}
.panel{position:relative;width:380px;height:855px;overflow:hidden}
.panel--features{background:var(--white);color:var(--ink)}
.panel--info{background:var(--dark);color:var(--white)}
.panel--cover{background:var(--darker);color:var(--white)}
.abs{position:absolute}
.hl{color:var(--orange)}
.heading{font-size:16px;font-weight:400;letter-spacing:.2px}
.heading .hl{font-weight:500;border-bottom:1.5px solid var(--orange)}
.checklist{list-style:none;left:34px;top:68px}
.checklist li{display:flex;align-items:center;gap:14px;font-size:12.5px;font-weight:500;height:26.5px}
.tick{width:12px;height:12px;flex:none}
.slogan{left:34px;top:300px;font-size:20px;line-height:24px}
.slogan .hl{font-weight:500}
.slogan span.line{display:inline-block;border-bottom:1.5px solid var(--orange);padding-right:8px}
.perfect{left:34px;top:372px}
.uses{top:410px;list-style:none}
.uses li{display:flex;align-items:flex-start;gap:10px;font-size:12.5px;font-weight:500;min-height:29px;line-height:14px}
.uses--a{left:36px}
.uses--b{left:220px}
.divider{left:203px;top:410px;width:2px;height:140px;background:var(--orange)}
.brands{left:20px;top:604px;width:340px;display:grid;grid-template-columns:repeat(3,1fr);row-gap:20px;text-align:center}
.brand{font-size:17px;font-weight:700;color:var(--ink);display:flex;align-items:center;justify-content:center;gap:6px;height:26px}
.brand i{width:9px;height:9px;border-radius:50%;background:var(--orange)}
.bottom-band{left:0;top:725px;width:380px;height:130px}
.browsers{left:0;top:785px;width:380px;height:70px;display:flex;align-items:center;justify-content:space-around;padding:0 18px}
.browsers span{color:var(--white);font-size:16px;font-weight:500;display:flex;align-items:center;gap:5px}
.browsers i{width:10px;height:10px;border:2px solid var(--white);border-radius:50%}
.info-heading{left:30px;top:40px}
.intro{left:30px;top:66px;width:324px;font-size:12.2px;line-height:14.2px;text-align:justify;color:#eee}
.logo{display:flex;align-items:center;gap:7px;font-family:'Roboto Condensed',sans-serif;font-weight:700;color:var(--white)}
.logo i{width:12px;height:12px;border-radius:50%;background:var(--orange)}
.logo--info{left:0;width:380px;top:270px;justify-content:center;font-size:14px}
.contact{left:26px;top:445px;width:330px;height:105px;border:1.5px solid var(--orange);border-radius:10px;text-align:center;font-size:12px;line-height:15px}
.contact-title{position:absolute;left:50%;top:-16px;transform:translateX(-50%);background:var(--dark);border:1.5px solid var(--orange);border-radius:9px;padding:5px 10px;font-size:15px;font-weight:500;white-space:nowrap}
.contact-addr{margin-top:28px;display:flex;justify-content:center;gap:10px;align-items:flex-start}
.contact-more{margin:12px 8px 0;text-align:justify;text-align-last:left;font-size:12px}
.contact-more em{color:var(--orange)}
.coverage{left:0;width:380px;top:572px;text-align:center}
.coverage h3{font-size:15px;font-weight:400}
.coverage h3 .hl{font-weight:500}
.coverage p{font-size:12px;margin-top:6px;color:#ddd}
.map{left:14px;top:618px;width:352px;height:170px;border:3px solid var(--orange);border-radius:8px;background:linear-gradient(135deg,#e2e2e2,#cfcfcf)}
.site-link{left:0;width:380px;top:810px;text-align:center;font-size:13px}
.site-link span{border-bottom:1.5px solid var(--orange);padding:0 4px 3px}
.cover-shapes{left:0;top:0;width:380px;height:855px}
.logo--cover{left:40px;top:86px;font-size:16px}
.cover-title{left:26px;top:480px;font-family:'Oswald',sans-serif;line-height:1}
.cover-title .reliable{font-size:36px;font-weight:500;display:flex;align-items:center;gap:10px}
.cover-title .reliable::after{content:"";width:70px;height:1.5px;background:var(--white);margin-top:14px}
.cover-title .speed{font-size:60px;font-weight:700;color:var(--orange);margin-top:6px}
.cover-title .service{font-size:32px;font-weight:500;margin-top:6px}
.cover-box{left:22px;top:630px;width:336px;height:172px;border:1.5px solid var(--white);border-radius:6px;text-align:center;font-family:'Roboto Condensed',sans-serif}
.cover-box .tech{color:var(--orange);font-size:22px;font-weight:700;margin-top:8px}
.cover-box .support{font-size:14px;margin-top:6px}
.cover-box .local{font-size:11px;font-style:italic}
.cover-box .hours{font-size:15px;font-weight:700;margin-top:16px}
.cover-box .phone{font-family:'Oswald',sans-serif;color:var(--orange);font-size:36px;font-weight:700;line-height:1.1}
</style>
</head>
<body>
<main class="spread">

  <section class="panel panel--features">
    <h2 class="heading abs" style="left:34px;top:38px"><span class="hl">RELIABLE INTERNET</span> SERVICE</h2>
    <ul class="checklist abs">
      <li><svg class="tick" viewBox="0 0 12 12"><circle cx="6" cy="6" r="5" fill="none" stroke="#f47b20" stroke-width="1.5"/><path d="M3.5 6l2 2 3-4" fill="none" stroke="#f47b20" stroke-width="1.5"/></svg>No Installation Charges</li>
      <li><svg class="tick" viewBox="0 0 12 12"><circle cx="6" cy="6" r="5" fill="none" stroke="#f47b20" stroke-width="1.5"/><path d="M3.5 6l2 2 3-4" fill="none" stroke="#f47b20" stroke-width="1.5"/></svg>Business and Residential Packages</li>
      <li><svg class="tick" viewBox="0 0 12 12"><circle cx="6" cy="6" r="5" fill="none" stroke="#f47b20" stroke-width="1.5"/><path d="M3.5 6l2 2 3-4" fill="none" stroke="#f47b20" stroke-width="1.5"/></svg>No Phone Line Required</li>
      <li><svg class="tick" viewBox="0 0 12 12"><circle cx="6" cy="6" r="5" fill="none" stroke="#f47b20" stroke-width="1.5"/><path d="M3.5 6l2 2 3-4" fill="none" stroke="#f47b20" stroke-width="1.5"/></svg>99.7% Network Uptime</li>
      <li><svg class="tick" viewBox="0 0 12 12"><circle cx="6" cy="6" r="5" fill="none" stroke="#f47b20" stroke-width="1.5"/><path d="M3.5 6l2 2 3-4" fill="none" stroke="#f47b20" stroke-width="1.5"/></svg>Always On and Highly Reliable</li>
      <li><svg class="tick" viewBox="0 0 12 12"><circle cx="6" cy="6" r="5" fill="none" stroke="#f47b20" stroke-width="1.5"/><path d="M3.5 6l2 2 3-4" fill="none" stroke="#f47b20" stroke-width="1.5"/></svg>24/7 Live Support By Local Nevadans</li>
      <li><svg class="tick" viewBox="0 0 12 12"><circle cx="6" cy="6" r="5" fill="none" stroke="#f47b20" stroke-width="1.5"/><path d="M3.5 6l2 2 3-4" fill="none" stroke="#f47b20" stroke-width="1.5"/></svg>Works With All Platforms (PC, Pomme, Kernix)</li>
      <li><svg class="tick" viewBox="0 0 12 12"><circle cx="6" cy="6" r="5" fill="none" stroke="#f47b20" stroke-width="1.5"/><path d="M3.5 6l2 2 3-4" fill="none" stroke="#f47b20" stroke-width="1.5"/></svg>All You Need Is A Router</li>
    </ul>
    <h2 class="slogan abs"><span class="hl">WE GO WHERE</span><br><span class="line">DSL AND CABLE CAN'T</span></h2>
    <h2 class="heading perfect abs"><span class="hl">OUR SERVICE IS</span> PERFECT FOR...</h2>
    <ul class="uses uses--a abs">
      <li><svg class="tick" viewBox="0 0 12 12"><circle cx="6" cy="6" r="5" fill="none" stroke="#f47b20" stroke-width="1.5"/><path d="M3.5 6l2 2 3-4" fill="none" stroke="#f47b20" stroke-width="1.5"/></svg>Chatterly</li>
      <li><svg class="tick" viewBox="0 0 12 12"><circle cx="6" cy="6" r="5" fill="none" stroke="#f47b20" stroke-width="1.5"/><path d="M3.5 6l2 2 3-4" fill="none" stroke="#f47b20" stroke-width="1.5"/></svg>Gaming</li>
      <li style="min-height:46px"><svg class="tick" viewBox="0 0 12 12"><circle cx="6" cy="6" r="5" fill="none" stroke="#f47b20" stroke-width="1.5"/><path d="M3.5 6l2 2 3-4" fill="none" stroke="#f47b20" stroke-width="1.5"/></svg>Stock Trading Online<br>Banking</li>
      <li><svg class="tick" viewBox="0 0 12 12"><circle cx="6" cy="6" r="5" fill="none" stroke="#f47b20" stroke-width="1.5"/><path d="M3.5 6l2 2 3-4" fill="none" stroke="#f47b20" stroke-width="1.5"/></svg>Downloading Music</li>
    </ul>
    <div class="divider abs"></div>
    <ul class="uses uses--b abs">
      <li><svg class="tick" viewBox="0 0 12 12"><circle cx="6" cy="6" r="5" fill="none" stroke="#f47b20" stroke-width="1.5"/><path d="M3.5 6l2 2 3-4" fill="none" stroke="#f47b20" stroke-width="1.5"/></svg>Telecommunicating</li>
      <li><svg class="tick" viewBox="0 0 12 12"><circle cx="6" cy="6" r="5" fill="none" stroke="#f47b20" stroke-width="1.5"/><path d="M3.5 6l2 2 3-4" fill="none" stroke="#f47b20" stroke-width="1.5"/></svg>Watching Movies</li>
      <li><svg class="tick" viewBox="0 0 12 12"><circle cx="6" cy="6" r="5" fill="none" stroke="#f47b20" stroke-width="1.5"/><path d="M3.5 6l2 2 3-4" fill="none" stroke="#f47b20" stroke-width="1.5"/></svg>Web Surfing</li>
      <li><svg class="tick" viewBox="0 0 12 12"><circle cx="6" cy="6" r="5" fill="none" stroke="#f47b20" stroke-width="1.5"/><path d="M3.5 6l2 2 3-4" fill="none" stroke="#f47b20" stroke-width="1.5"/></svg>Email</li>
      <li><svg class="tick" viewBox="0 0 12 12"><circle cx="6" cy="6" r="5" fill="none" stroke="#f47b20" stroke-width="1.5"/><path d="M3.5 6l2 2 3-4" fill="none" stroke="#f47b20" stroke-width="1.5"/></svg>VoIP</li>
    </ul>
    <div class="brands abs">
      <span class="brand"><i></i>Chatterly</span>
      <span class="brand">Streamla</span>
      <span class="brand">Appvale</span>
      <span class="brand">Meetwell</span>
      <span class="brand">TradeNest</span>
      <span class="brand">Callory</span>
      <span class="brand" style="grid-column:1/3">Tunebox</span>
      <span class="brand" style="margin-left:-110px">Flixtide</span>
    </div>
    <svg class="bottom-band abs" viewBox="0 0 380 130" preserveAspectRatio="none">
      <polygon points="0,0 380,0 380,20 0,60" fill="#ffffff"/>
      <polygon points="0,35 380,18 380,60 0,60" fill="#1a1a1a"/>
      <polygon points="0,60 190,58 380,50 380,130 0,130" fill="#f47b20"/>
    </svg>
    <div class="browsers abs">
      <span><i></i>Orbit</span><span>Compass</span><span>Seeker</span><span>Foxtail</span><span>Prism</span>
    </div>
  </section>

  <section class="panel panel--info">
    <h2 class="heading info-heading abs"><span class="hl">TRUE HIGH SPEED</span> INTERNET</h2>
    <p class="intro abs">Tallow Linkworks provides true High Speed, High Reliability Internet service for residential and business customers in the Northern Nevada area. Outstanding customer service combined with a state-of-the-art network and highly competitive rates make us the preferred choice in our service areas.</p>
    <div class="logo logo--info abs"><i></i>Tallow-Linkworks.com</div>
    <div class="contact abs">
      <div class="contact-title">TALLOW LINKWORKS INC.</div>
      <div class="contact-addr">
        <svg width="12" height="14" viewBox="0 0 12 14"><path d="M6 13C2 8 1 6.5 1 5a5 5 0 0 1 10 0c0 1.5-1 3-5 8z" fill="#f47b20"/><circle cx="6" cy="5" r="1.8" fill="#232323"/></svg>
        <span>14 N Birch St Marlow,<br>NV 89400</span>
      </div>
      <p class="contact-more">For Additional Information About Services, Service Areas Or How To Get Started Call <em>775.555.0148</em></p>
    </div>
    <div class="coverage abs">
      <h3><span class="hl">COVERAGE</span> MAP</h3>
      <p>We are continua expanding our service area</p>
    </div>
    <div class="map abs" role="img" aria-label="Street map of the town centre showing the service coverage area and office location"></div>
    <p class="site-link abs"><span>Visit Our Website For Exact Coverage Areas</span></p>
  </section>

  <section class="panel panel--cover">
    <svg class="cover-shapes abs" viewBox="0 0 380 855">
      <polygon points="0,105 0,170 150,132" fill="#f47b20"/>
      <polygon points="0,170 380,118 380,410 0,460" fill="#b98a68" role="img" aria-label="Photo of a young man working on a laptop at a desk with a lamp and mug"/>
      <polygon points="380,350 380,440 210,435" fill="#f47b20"/>
    </svg>
    <div class="logo logo--cover abs"><i></i>Tallow-Linkworks.com</div>
    <div class="cover-title abs">
      <div class="reliable">Reliable</div>
      <div class="speed">HIGH SPEED</div>
      <div class="service">INTERNET SERVICE</div>
    </div>
    <div class="cover-box abs">
      <div class="tech">State-Of-The-Art Technology</div>
      <div class="support">Combined With Real Customer Service</div>
      <div class="local">By Local Nevadans</div>
      <div class="hours">Support Available 24 Hours A Day</div>
      <div class="phone">775 555 0148</div>
    </div>
  </section>

</main>
</body>
</html>
```